Stonefield Partners Business Card Design

We are looking for a new business card design, we are not happy with our current design. We are a boutique management consulting firm and our clients are typically fortune 500 companies.

I have attached the current front and back that we have as well as a version of our logo that can be used. I am trying to get a higher resolution version of the logo file to upload to the project.

Target Market(s)

Fortune 500 companies are our primary client base. Financial services, life sciences, pharmaceuticals and telecom companies are

Industry/Entity Type

Management Consulting

Contact Information for Business Card

We are trying to communicate a high degree of professionalism, a somewhat minimalist perhaps with some air of whimsy (without overdoing it). Attached is the current design, front and back as well as logos. I like the current back of the card and assume we will keep the phrase the same.

From a color palette perspective, I prefer to stay with a gray scale as they are today.

Font styles to use
Sans Serif

Colors
1b1b1b
474747
ffffff

Requirements
Must have
• Two sided business card design. File format should be something that can be used outside of Photoshop like MS Publisher so that they can be edited with personal information.
• Font should be calibri or something very similar and should be available within MS Office
Should not have
• No other logos or graphics outside of the logo provided.

```html
<!DOCTYPE html>
<html lang="en">
<head>
<meta charset="utf-8">
<title>Stonefield Partners — Business Card</title>
<link rel="stylesheet" href="https://fonts.googleapis.com/css2?family=Carlito:wght@400;700&display=swap">
<style>
  :root {
    --ink: #1b1b1b;
    --ink-soft: #474747;
    --paper: #ffffff;
    --paper-back: #f6f6f6;
    --strip: #f2f2f2;
    --faint: #dedede;
    --stage: #3b302c;
  }
  * { margin: 0; padding: 0; box-sizing: border-box; }
  html, body {
    width: 1200px; height: 750px; overflow: hidden;
    background: var(--stage);
    font-family: "Carlito", "Calibri", sans-serif;
  }
  .canvas { position: relative; width: 1200px; height: 750px; }
  .card {
    position: absolute; left: 390px; width: 461px; height: 263px;
    overflow: hidden; box-shadow: 0 2px 6px rgba(0,0,0,.35);
  }
  /* Front */
  .card-front { top: 107px; background: var(--ink); color: var(--paper); }
  .card-front .strip {
    position: absolute; left: 0; top: 0; width: 43px; height: 100%;
    background: var(--strip);
  }
  .brand-dot {
    position: absolute; left: 22px; top: 28px; width: 36px; height: 36px;
    border-radius: 50%; background: var(--paper); border: 4px solid var(--ink);
  }
  .brand-name {
    position: absolute; left: 70px; top: 23px;
    font-size: 38px; font-weight: 700; line-height: 1; letter-spacing: -.3px;
  }
  .front-body { position: absolute; left: 70px; top: 78px; }
  .person-name { font-size: 17px; font-weight: 700; line-height: 20px; }
  .person-role { font-size: 13px; line-height: 18px; }
  .contacts { list-style: none; margin-top: 8px; }
  .contacts li {
    display: flex; align-items: center; gap: 5px;
    font-size: 12.5px; line-height: 17.5px;
  }
  .contacts svg { width: 12px; height: 12px; fill: var(--paper); flex: none; }
  .office { margin-top: 10px; font-size: 12.5px; line-height: 16px; }
  .office strong { display: block; font-weight: 700; margin-bottom: 1px; }

  /* Back */
  .card-back { top: 398px; background: var(--paper-back); color: var(--ink); }
  .back-circle {
    position: absolute; left: 264px; top: 24px; width: 190px; height: 190px;
    border-radius: 50%; background: var(--faint);
  }
  .back-name {
    position: absolute; left: 24px; top: 153px;
    font-size: 48px; font-weight: 700; line-height: 1; letter-spacing: -.5px;
  }
  .tagline {
    position: absolute; left: 24px; top: 201px; width: 230px;
    text-align: center; font-size: 16.5px; line-height: 21px; color: var(--ink);
  }
</style>
</head>
<body>
<main class="canvas">
  <section class="card card-front" aria-label="Card front">
    <div class="strip"></div>
    <div class="brand-dot"></div>
    <div class="brand-name">Stonefield</div>
    <div class="front-body">
      <p class="person-name">Marcus Hale</p>
      <p class="person-role">Los Angeles Office | Managing Director</p>
      <ul class="contacts">
        <li><svg viewBox="0 0 16 16" aria-hidden="true"><path d="M3.6 1.2l2.3 2.6c.4.4.4 1 0 1.4L4.8 6.4c.9 2 2.6 3.7 4.6 4.6l1.2-1.1c.4-.4 1-.4 1.4 0l2.6 2.3c.4.4.4 1 0 1.4l-1.4 1.4C11 16.9 0 6 .3 3.8L1.7 2.2c.5-.4 1.5-.4 1.9-1z"/></svg>206.555.0142</li>
        <li><svg viewBox="0 0 16 16" aria-hidden="true"><path d="M1 3h14v10H1z M1.5 3.5L8 9l6.5-5.5" stroke="#1b1b1b" stroke-width="1.2"/></svg>mhale@stonefieldpartners.com</li>
        <li><svg viewBox="0 0 16 16" aria-hidden="true"><circle cx="8" cy="8" r="7"/><path d="M1 8h14M8 1c-3 3-3 11 0 14M8 1c3 3 3 11 0 14" stroke="#1b1b1b" stroke-width="1.1" fill="none"/></svg>www.stonefieldpartners.com</li>
      </ul>
      <p class="office"><strong>Stonefield Partners, Inc.</strong>Headquarters, 218 Harbor View Road<br>Suite 210, Port Alden, WA 98000</p>
    </div>
  </section>

  <section class="card card-back" aria-label="Card back">
    <div class="back-circle"></div>
    <div class="back-name">Stonefield</div>
    <p class="tagline">The preferred choice<br>for leadership’s top priorities</p>
  </section>
</main>
</body>
</html>
```